Faltblatt Hausmeisterei
Zielgruppe
Ich benötige einen neuen Flyer für eine Hausmeisterei http://www.objektpflege-kernwald.de/.
Zielgruppe ist hier nicht nur der Privathaushalt mit Renovierungen oder Reparaturen sondern auch eine Firma oder Kanzlei oder Hausverwaltung welche eine Objektbetreuung vergibt.
Es soll wieder ein beidseitiger Faltblattflyer werden. Hinsichtlich Farbe und Design Inhalt bin ich jedoch offen.
Aufgabenstellung
Ich habe unseren alten Faltblattflyer angefügt der Flyer sollte in diese Richtung gehen jedoch etwas moderner sein.

```html
<!DOCTYPE html>
<html lang="de">
<head>
<meta charset="utf-8">
<title>Faltblatt Hausmeisterei Kernwald</title>
<link rel="stylesheet" href="https://fonts.googleapis.com/css2?family=Jost:wght@400;500;600;700;800&display=swap">
<style>
  :root {
    --yellow: #fcd000;
    --red: #e3300f;
    --green: #7aab2d;
    --green-text: #7aa82a;
    --ink: #111111;
    --white: #ffffff;
    --page: #ffffff;
  }
  * { box-sizing: border-box; margin: 0; padding: 0; }
  html, body { width: 1200px; height: 1175px; overflow: hidden; background: var(--page); }
  body { position: relative; font-family: "Jost", sans-serif; color: var(--ink); }

  .panel {
    position: absolute; top: 71px; width: 479px; height: 1015px; overflow: hidden;
    background: var(--white);
    box-shadow: 0 6px 28px rgba(0,0,0,.18);
  }
  .panel--front { left: 84px; }
  .panel--back { left: 640px; }
  .panel__bg { position: absolute; inset: 0; width: 100%; height: 100%; }

  .abs { position: absolute; left: 0; right: 0; text-align: center; }
  .tilt { transform: rotate(-1.9deg); }

  /* front */
  .hero-title { top: 26px; line-height: 1; font-weight: 700; }
  .hero-title__lead { font-size: 35px; }
  .hero-title__main { font-size: 54px; font-weight: 800; color: var(--red); margin: 4px 0 2px; }
  .hero-title__sub { font-size: 35px; }
  .hero-photo { position: absolute; left: 0; top: 170px; width: 479px; height: 610px; }

  .cta { font-weight: 700; line-height: 1.15; }
  .cta__call { color: var(--red); font-size: 28px; }
  .cta__phone { font-size: 24px; }
  .panel--front .cta { top: 780px; }
  .panel--back .cta { top: 805px; }
  .panel--back .cta__call { font-size: 30px; }
  .panel--back .cta__phone { font-size: 26px; }

  .brand { top: 900px; display: flex; align-items: center; justify-content: center; gap: 18px; color: var(--white); }
  .brand__mark { width: 112px; height: 62px; background: var(--white); }
  .brand__text { text-align: left; }
  .brand__name { font-size: 40px; font-weight: 800; line-height: 1; letter-spacing: 1px; }
  .brand__tag { font-size: 13px; font-weight: 400; margin-top: 4px; }
  .web { font-weight: 700; color: var(--white); font-size: 20px; }
  .panel--front .web { top: 978px; }

  /* back */
  .section-title { top: 18px; line-height: 1; font-weight: 700; }
  .section-title__lead { font-size: 26px; }
  .section-title__main { font-size: 36px; font-weight: 800; color: var(--red); }

  .service { position: absolute; width: 210px; }
  .service__photo { width: 202px; height: 127px; }
  .service__head { color: var(--green-text); font-weight: 600; font-size: 16px; line-height: 1.3; margin-top: 18px; letter-spacing: .2px; }
  .service__list { list-style: none; margin-top: 4px; }
  .service__list li { position: relative; padding-left: 18px; font-size: 15.5px; line-height: 1.3; margin-bottom: 4px; }
  .service__list li::before { content: ""; position: absolute; left: 6px; top: 9px; width: 4px; height: 4px; border-radius: 50%; background: var(--ink); }
  .service__list li.small { font-size: 11.5px; line-height: 1.45; }
  .service__list li.small::before { top: 6px; }
  .col-a { left: 29px; }
  .col-b { left: 250px; }
  .row-1 { top: 121px; }
  .row-2 { top: 460px; }
  .row-1.col-b .service__head { margin-top: 18px; }

  .contact { top: 903px; color: var(--white); font-size: 15px; line-height: 1.4; font-weight: 400; }
  .contact__name { font-weight: 700; }
  .panel--back .web { top: 982px; font-size: 21px; }
</style>
</head>
<body>

<section class="panel panel--front">
  <svg class="panel__bg" viewBox="0 0 479 1015" preserveAspectRatio="none" aria-hidden="true">
    <polygon points="0,0 479,0 479,178 0,194" fill="var(--yellow)"/>
    <polygon points="0,772 479,757 479,1015 0,1015" fill="var(--yellow)"/>
    <polygon points="0,861 479,846 479,1015 0,1015" fill="var(--green)"/>
  </svg>
  <div class="hero-photo" role="img" aria-label="Foto: Handwerker mit Schirmmütze montiert ein Klimagerät an der Wand"
       style="background:linear-gradient(160deg,#d9c7bb 0%,#e8dcd6 35%,#c9957a 60%,#4a5d80 100%);clip-path:polygon(0 4%,100% 1.5%,100% 96.8%,0 99.2%);"></div>
  <h1 class="abs hero-title tilt">
    <span class="hero-title__lead" style="display:block">Ihr engagierter</span>
    <span class="hero-title__main" style="display:block">Hausmeister-</span>
    <span class="hero-title__sub" style="display:block">Familienbetrieb</span>
  </h1>
  <div class="abs cta tilt">
    <div class="cta__call">JETZT ANRUFEN!</div>
    <div class="cta__phone">Sofort-Beratung 0170 - 348 52 61</div>
  </div>
  <div class="abs brand">
    <div class="brand__mark"></div>
    <div class="brand__text">
      <div class="brand__name">KERNWALD</div>
      <div class="brand__tag">Ihr engagierter Familien-Handwerksbetrieb!</div>
    </div>
  </div>
  <div class="abs web">www.objektpflege-kernwald.de</div>
</section>

<section class="panel panel--back">
  <svg class="panel__bg" viewBox="0 0 479 1015" preserveAspectRatio="none" aria-hidden="true">
    <polygon points="0,0 479,0 479,87 0,101" fill="var(--yellow)"/>
    <polygon points="0,797 479,782 479,1015 0,1015" fill="var(--yellow)"/>
    <polygon points="0,886 479,871 479,1015 0,1015" fill="var(--green)"/>
  </svg>
  <h2 class="abs section-title tilt">
    <span class="section-title__lead" style="display:block">Unsere</span>
    <span class="section-title__main" style="display:block">Leistungen</span>
  </h2>

  <article class="service col-a row-1">
    <div class="service__photo" role="img" aria-label="Foto: Handwerker mit Werkzeuggürtel macht Notizen auf einem Klemmbrett" style="background:linear-gradient(135deg,#7a4a33,#5a7598 55%,#c98a3a)"></div>
    <h3 class="service__head">HAUSMEISTERSERVICE<br>+ MEHR</h3>
    <ul class="service__list">
      <li>Hausmeisterservice</li>
      <li>Reparaturdienste</li>
      <li>Renovierungen</li>
      <li class="small">seit über 15 Jahren zuverlässiger Partner vor Ort für Vermieter, Hauseigentümer/-verwaltungen &amp; Behörden</li>
    </ul>
  </article>

  <article class="service col-b row-1">
    <div class="service__photo" role="img" aria-label="Foto: Gärtner schneidet eine Hecke mit der Heckenschere" style="background:linear-gradient(135deg,#2f6b2a,#4f8f3a 55%,#1e6e50)"></div>
    <h3 class="service__head">GARTEN- &amp; BEETPFLEGE</h3>
    <ul class="service__list">
      <li>Rasenpflege, Düngen, Wässern, Vertikutieren</li>
      <li>Heckenschneiden</li>
      <li>Bäume fällen</li>
      <li>Laub abräumen, Dachrinnen-Reinigung</li>
      <li>Pflasterarbeiten</li>
    </ul>
  </article>

  <article class="service col-a row-2">
    <div class="service__photo" role="img" aria-label="Foto: Gerümpel vor einer Ziegelwand mit Schild „Wir entrümpeln für Sie!“" style="background:linear-gradient(135deg,#8c4a32,#a87a4c 50%,#3b4e6a)"></div>
    <h3 class="service__head">ENTRÜMPELUNGEN<br>+ MEHR</h3>
    <ul class="service__list">
      <li>Keller-, Wohnungs- &amp; Büroauflösungen</li>
      <li>kurzfristig &amp; zum fairen Preis</li>
      <li class="small">seit fast 20 Jahren zuverlässiger Partner vor Ort für Vermieter, Haus-eigentümer/-verwalter &amp; Behörden</li>
    </ul>
  </article>

  <article class="service col-b row-2">
    <div class="service__photo" role="img" aria-label="Foto: Handwerker verlegt Laminat in einem hellen Raum" style="background:linear-gradient(160deg,#f2efe9,#e6d6bf 55%,#c9a26b)"></div>
    <h3 class="service__head">RENOVIERUNGEN</h3>
    <ul class="service__list">
      <li>Malern, Türen und Heizkörper lackieren</li>
      <li>Teppich/Laminat verlegen</li>
      <li>Reparaturdienste, Umzugshilfe &amp; Entrümpelungen</li>
    </ul>
  </article>

  <div class="abs cta tilt">
    <div class="cta__call">JETZT ANRUFEN!</div>
    <div class="cta__phone">Sofort-Beratung 0170 - 348 52 61</div>
  </div>
  <address class="abs contact" style="font-style:normal">
    <div class="contact__name">Hausmeisterei Kernwald</div>
    <div>Lindenhofer Str. 24 | 80999 München</div>
    <div>service@objektpflege-kernwald.de</div>
  </address>
  <div class="abs web">www.objektpflege-kernwald.de</div>
</section>

</body>
</html>
```